Fernwood Chiropractic
letterhead/business cards
Project: Fernwood Chiropractic
Fernwood Chiropractic - Health
Creative Brief
Professional
Dr. Gavin P. Holcombe
Chiropractor
72 Alder Court, Unit 5, Maplecrest, ST 00000
drholcombe@fernwoodchiro-example.com
www.fernwoodchiro-example.com

```html
<!DOCTYPE html>
<html lang="en">
<head>
<meta charset="utf-8">
<title>Fernwood Chiropractic – Business Cards</title>
<link rel="stylesheet" href="https://fonts.googleapis.com/css2?family=Cinzel:wght@400;700&display=swap">
<style>
  :root{
    --bg:#e4e2de;
    --paper:#fbfbfb;
    --glass:rgba(255,255,255,0.38);
    --green-light:#8fd14f;
    --green:#4bb02c;
    --green-dark:#1f8a1c;
    --silver-light:#f4f4f4;
    --silver:#bdbdbd;
    --silver-dark:#8b8b8b;
    --brand-blue:#2b5f9f;
    --name-grey:#5a5a5a;
    --white:#ffffff;
  }
  *{box-sizing:border-box;margin:0;padding:0}
  html,body{width:1200px;height:730px;overflow:hidden}
  body{background:var(--bg);font-family:"Cinzel",serif;position:relative}
  .card{
    position:absolute;width:528px;height:272px;border-radius:20px;overflow:hidden;
    box-shadow:0 4px 14px rgba(0,0,0,0.18);
  }
  .card--paper{background:var(--paper)}
  .card--glass{background:var(--glass);border:1px solid rgba(255,255,255,0.7)}
  .card--front-paper{left:36px;top:53px}
  .card--front-glass{left:636px;top:53px}
  .card--back-paper{left:36px;top:396px}
  .card--back-glass{left:636px;top:396px}

  .brand{
    position:absolute;left:0;right:0;top:34px;display:flex;justify-content:center;align-items:center;gap:14px;
  }
  .brand__dot{width:44px;height:44px;border-radius:50%;background:var(--green)}
  .brand__name{
    color:var(--brand-blue);font-weight:700;font-size:26px;line-height:1.05;letter-spacing:0.5px;
  }
  .brand__name span{display:block;font-size:22px}

  .band{
    position:absolute;left:0;right:0;bottom:0;
    background:linear-gradient(180deg,var(--green-light) 0%,var(--green) 45%,var(--green-dark) 100%);
  }
  .band::before{
    content:"";position:absolute;left:0;right:0;top:0;height:5px;
    background:linear-gradient(90deg,var(--silver-dark),var(--silver-light) 50%,var(--silver-dark));
  }
  .band--front{height:128px}
  .band--back{height:112px}

  .nameplate{
    position:absolute;left:0;right:0;top:5px;height:30px;
    background:linear-gradient(180deg,var(--silver-light),var(--silver));
    display:flex;align-items:center;justify-content:center;
    font-size:12px;letter-spacing:1.5px;color:var(--name-grey);
  }
  .contacts{
    position:absolute;left:24px;right:24px;top:52px;color:var(--white);
    font-size:9.5px;letter-spacing:0.4px;line-height:1;
    display:flex;flex-direction:column;gap:10px;
  }
  .contacts__row{display:flex;align-items:center;gap:14px;white-space:nowrap}
  .contacts__item{display:flex;align-items:center;gap:5px}
  .icon{width:11px;height:11px;flex:none}

  .url{
    position:absolute;left:0;right:0;top:46px;text-align:center;color:var(--white);
    font-size:13px;letter-spacing:3px;
  }
  .card--back-glass .band{opacity:0.75}
  .brand--mirrored{transform:scaleX(-1);opacity:0.35;top:48px}
</style>
</head>
<body>

<section class="card card--paper card--front-paper" aria-label="Business card front">
  <div class="brand">
    <span class="brand__dot"></span>
    <div class="brand__name">FERNWOOD<span>CHIROPRACTIC</span></div>
  </div>
  <div class="band band--front">
    <div class="nameplate">DR. GAVIN P. HOLCOMBE | CHIROPRACTOR</div>
    <div class="contacts">
      <div class="contacts__row">
        <span class="contacts__item">
          <svg class="icon" viewBox="0 0 12 12"><path d="M6 0.5a3.8 3.8 0 0 0-3.8 3.8C2.2 7.2 6 11.5 6 11.5s3.8-4.3 3.8-7.2A3.8 3.8 0 0 0 6 0.5zm0 5.3a1.5 1.5 0 1 1 0-3 1.5 1.5 0 0 1 0 3z" fill="#fff"/></svg>
          72 Alder Court, Unit 5, Maplecrest, ST 00000
        </span>
      </div>
      <div class="contacts__row">
        <span class="contacts__item">
          <svg class="icon" viewBox="0 0 12 12"><path d="M2.6 0.8l1.9 2.4-1 1.3a7 7 0 0 0 4 4l1.3-1 2.4 1.9-1 1.8C5.6 11.2 0.8 6.4 0.8 1.8z" fill="#fff"/></svg>
          (555) 010-0148
        </span>
        <span class="contacts__item">
          <svg class="icon" viewBox="0 0 12 12"><rect x="0.8" y="2.2" width="10.4" height="7.6" rx="1" fill="none" stroke="#fff"/><path d="M1 2.6 6 6.6 11 2.6" fill="none" stroke="#fff"/></svg>
          drholcombe@fernwoodchiro-example.com
        </span>
      </div>
    </div>
  </div>
</section>

<section class="card card--glass card--front-glass" aria-label="Clear business card front">
  <div class="brand">
    <span class="brand__dot"></span>
    <div class="brand__name">FERNWOOD<span>CHIROPRACTIC</span></div>
  </div>
  <div class="band band--front">
    <div class="nameplate">DR. GAVIN P. HOLCOMBE | CHIROPRACTOR</div>
    <div class="contacts">
      <div class="contacts__row">
        <span class="contacts__item">
          <svg class="icon" viewBox="0 0 12 12"><path d="M6 0.5a3.8 3.8 0 0 0-3.8 3.8C2.2 7.2 6 11.5 6 11.5s3.8-4.3 3.8-7.2A3.8 3.8 0 0 0 6 0.5zm0 5.3a1.5 1.5 0 1 1 0-3 1.5 1.5 0 0 1 0 3z" fill="#fff"/></svg>
          72 Alder Court, Unit 5, Maplecrest, ST 00000
        </span>
      </div>
      <div class="contacts__row">
        <span class="contacts__item">
          <svg class="icon" viewBox="0 0 12 12"><path d="M2.6 0.8l1.9 2.4-1 1.3a7 7 0 0 0 4 4l1.3-1 2.4 1.9-1 1.8C5.6 11.2 0.8 6.4 0.8 1.8z" fill="#fff"/></svg>
          (555) 010-0148
        </span>
        <span class="contacts__item">
          <svg class="icon" viewBox="0 0 12 12"><rect x="0.8" y="2.2" width="10.4" height="7.6" rx="1" fill="none" stroke="#fff"/><path d="M1 2.6 6 6.6 11 2.6" fill="none" stroke="#fff"/></svg>
          drholcombe@fernwoodchiro-example.com
        </span>
      </div>
    </div>
  </div>
</section>

<section class="card card--paper card--back-paper" aria-label="Business card back">
  <div class="brand">
    <span class="brand__dot"></span>
    <div class="brand__name">FERNWOOD<span>CHIROPRACTIC</span></div>
  </div>
  <div class="band band--back">
    <div class="url">www.fernwoodchiro-example.com</div>
  </div>
</section>

<section class="card card--glass card--back-glass" aria-label="Clear business card back">
  <div class="brand brand--mirrored">
    <span class="brand__dot"></span>
    <div class="brand__name">FERNWOOD<span>CHIROPRACTIC</span></div>
  </div>
  <div class="band band--back">
    <div class="url">www.fernwoodchiro-example.com</div>
  </div>
</section>

</body>
</html>
```